Business Card Design

Verdessa is a floral design company for weddings and special events.
Colours wanted are dark grey, aqua blue, white and black.
dark grey for the background, and the Verdessa in the aqua blue, rest of the writing in white and black etc.

Our floral design style is Rustic, textural, natural,
Wanting some kind of simplistic flower symbol next to the Verdessa see pictures.

Hi im so sorry I've changed some criteria. been confused on how this site works and what i want!! hope this is more straight forward. I also need clip art of the simple floral design i attached for my web site and also car magnets. thank you thank you thank YOU!!!! cherrs Bree

I have attached x5 ideas on where to place the lotus flower next to and around the verdessa. please use simliar colours of the flower as pictured. please cut out the white back ground from the flower. use only petals. use only lotus or the other icon provided per idea. still deciding on which one to use so waiting to see what looks best with your designs. thank you so very much in advance.!! Kindest REgards Bree

hi i am currently getting a logo design made through this also so can we wait until it is complete before any revisions are made. sorry about the delay!! thank you thank you thank you!! kind regards Bree

Reason: im having a logo made also to use on the cards. please hold off on any designs until this is received. thank you and so sorry about this!! cheers bR

Target Market(s)

modern elegant professional

Industry/Entity Type

Floral

Contact Information for Business Card

Front:
verdessa floral design (all lower case) floral design in smaller writting)
www.verdessafloraldesign.example.au

Back:
Wedding and event design

Bridget - 0498265140
verdessa@mailcove.example.au
Pauline-0455839061
floristpaulinecrowe@postly.example.com

Wattle Creek, Sunrise Coast, QLD

Font styles to use
Other font styles liked:
• corben, cookie

Colors
87d0c7
34b8a4
eaf2ce
ffffff
e4daeb
cfdeed

Requirements
Must have
• ; dark grey for back ground. or possible all white?
;verdessa floral designs in lower case and in blue' green aqua colour. all other writing in white.
icon which i can also use on the website. see pictures(i want to use the same on my web site.. if you can please make me an clip art icon also?
Nice to have
• simple elegant, earthy, flower icon
or second option icon of lotus looking flower verdessa inside
fonts please: verdessa floral design in (corben)
all writing on the back in (cookie)
maybe have the same icon clip art provided faintly on the back, bold on the front?
i also need car magnets to

```html
<!DOCTYPE html>
<html lang="en">
<head>
<meta charset="utf-8">
<title>Verdessa Floral Design – Business Cards</title>
<link rel="stylesheet" href="https://fonts.googleapis.com/css2?family=Cinzel:wght@400;500&family=Pinyon+Script&display=swap">
<style>
  :root {
    --backdrop: #3b3b3d;
    --card: #ffffff;
    --aqua: #84d3c9;
    --aqua-deep: #5fb0a6;
    --teal-text: #2bb5a3;
    --ink: #1f2322;
    --rose: #e8638f;
    --rose-soft: #f4a9c1;
    --lily: #f6f3ee;
    --leaf: #5f8a3d;
    --heather: #b04a7a;
  }
  * { box-sizing: border-box; margin: 0; padding: 0; }
  html, body {
    width: 1200px; height: 900px; overflow: hidden;
    background: var(--backdrop);
  }
  .sheet {
    position: relative; width: 1200px; height: 900px;
    display: flex; flex-direction: column; align-items: center;
    justify-content: center; gap: 60px;
  }
  .card {
    position: relative; width: 700px; height: 400px;
    background: var(--card); overflow: hidden;
    box-shadow: 0 14px 30px rgba(0,0,0,.45);
  }

  /* Front */
  .front-band {
    position: absolute; left: 0; top: 0; bottom: 0; width: 104px;
    background: var(--aqua);
  }
  .front-band .flourish {
    position: absolute; inset: 20px 14px;
    background: linear-gradient(180deg, rgba(95,176,166,.7), rgba(95,176,166,.35) 60%, rgba(95,176,166,.6));
    border-radius: 40px;
  }
  .brand-name {
    position: absolute; left: 190px; top: 62px;
    font-family: "Pinyon Script", cursive; font-size: 56px;
    color: var(--ink); font-weight: 400; white-space: nowrap;
  }
  .brand-url {
    position: absolute; left: 212px; top: 148px;
    font-family: "Cinzel", serif; font-size: 14px; letter-spacing: .08em;
    color: var(--ink);
  }
  .bouquet {
    position: absolute;
    background:
      radial-gradient(circle at 28% 45%, var(--rose) 0 9%, transparent 10%),
      radial-gradient(circle at 55% 38%, var(--rose) 0 8%, transparent 9%),
      radial-gradient(circle at 48% 75%, var(--rose) 0 9%, transparent 10%),
      radial-gradient(circle at 40% 55%, var(--lily) 0 18%, transparent 19%),
      radial-gradient(circle at 70% 60%, var(--lily) 0 12%, transparent 13%),
      radial-gradient(circle at 60% 85%, var(--heather) 0 5%, transparent 6%),
      radial-gradient(ellipse at 50% 60%, #a9c48a 0 40%, rgba(95,138,61,.0) 70%);
  }
  .front-bouquet {
    left: 120px; top: 190px; width: 400px; height: 240px;
    border-radius: 50% 50% 0 0 / 60% 60% 0 0;
  }

  /* Back */
  .back-band {
    position: absolute; left: 0; top: 0; right: 0; height: 104px;
    background: var(--aqua);
  }
  .back-band .flourish {
    position: absolute; left: 24px; right: 24px; top: 14px; bottom: 14px;
    background: linear-gradient(90deg, rgba(95,176,166,.55), rgba(95,176,166,.25) 50%, rgba(95,176,166,.55));
    border-radius: 40px;
  }
  .tagline {
    position: absolute; right: 36px; top: 22px;
    font-family: "Pinyon Script", cursive; font-size: 44px;
    color: var(--ink); white-space: nowrap;
  }
  .contact-person {
    position: absolute; top: 124px;
    font-family: "Cinzel", serif; text-align: center;
  }
  .contact-person .name { font-size: 13px; letter-spacing: .1em; color: var(--ink); }
  .contact-person .phone { font-size: 15px; letter-spacing: .06em; color: var(--teal-text); }
  .person-one { left: 118px; }
  .person-two { left: 380px; }
  .contact-lines {
    position: absolute; left: 40px; top: 186px; list-style: none;
    font-family: "Cinzel", serif; color: var(--ink);
  }
  .contact-lines li { display: flex; align-items: center; gap: 12px; margin-bottom: 8px; }
  .contact-lines svg { width: 16px; height: 16px; flex: none; }
  .email-main { font-size: 24px; letter-spacing: .08em; }
  .address, .email-alt { font-size: 14px; letter-spacing: .07em; }
  .back-bouquet {
    right: -10px; bottom: -20px; width: 300px; height: 200px;
    border-radius: 50% 0 0 0 / 60% 0 0 0;
  }
</style>
</head>
<body>
<main class="sheet">
  <section class="card card-front" aria-label="Business card front">
    <div class="front-band"><div class="flourish" role="img" aria-label="Grey scrolling floral flourish on aqua band"></div></div>
    <h1 class="brand-name">Verdessa Floral Design</h1>
    <p class="brand-url">WWW.VERDESSAFLORALDESIGN.EXAMPLE.AU</p>
    <div class="bouquet front-bouquet" role="img" aria-label="Bouquet of pink roses, white lilies and green buds"></div>
  </section>

  <section class="card card-back" aria-label="Business card back">
    <div class="back-band">
      <div class="flourish" role="img" aria-label="Faint grey scrolling floral flourish on aqua band"></div>
      <p class="tagline">Wedding and event specialists</p>
    </div>
    <div class="contact-person person-one">
      <p class="name">BRIDGET</p>
      <p class="phone">0498265140</p>
    </div>
    <div class="contact-person person-two">
      <p class="name">PAULINE</p>
      <p class="phone">0455839061</p>
    </div>
    <ul class="contact-lines">
      <li class="email-main">
        <svg viewBox="0 0 16 16" aria-hidden="true"><circle cx="8" cy="8" r="7" fill="none" stroke="#1f2322" stroke-width="1.3"/><ellipse cx="8" cy="8" rx="3" ry="7" fill="none" stroke="#1f2322" stroke-width="1.1"/><line x1="1" y1="8" x2="15" y2="8" stroke="#1f2322" stroke-width="1.1"/></svg>
        VERDESSA@MAILCOVE.EXAMPLE.AU
      </li>
      <li class="address">
        <svg viewBox="0 0 16 16" aria-hidden="true"><path d="M8 1a5 5 0 0 1 5 5c0 4-5 9-5 9S3 10 3 6a5 5 0 0 1 5-5z" fill="#1f2322"/><circle cx="8" cy="6" r="1.8" fill="#fff"/></svg>
        WATTLE CREEK, SUNRISE COAST, QLD
      </li>
      <li class="email-alt">
        <svg viewBox="0 0 16 16" aria-hidden="true"><rect x="1" y="3" width="14" height="10" fill="#1f2322"/><path d="M1 3l7 6 7-6" fill="none" stroke="#fff" stroke-width="1.1"/></svg>
        FLORISTPAULINECROWE@POSTLY.EXAMPLE.COM
      </li>
    </ul>
    <div class="bouquet back-bouquet" role="img" aria-label="Bouquet of pink roses and white lilies with greenery"></div>
  </section>
</main>
</body>
</html>
```